Kyvex brochure for corporate sector

Our company provides audio visual solutions to the corporate and government markets across Australia. Interactive touch screens are popular in schools and education sectors but are slow to adopt in the corporate market. We wish to create an attention-grabbing A4 single sided colour brochure to promote a state-of-the-art large-format touchscreen product to the financial sector - more specifically for financial planners, board meeting etc. These are available on 55",65",70" and 84" sizes making them ideal for meetings to interact with customers while impressing them with technology.
We have attached a brochure that details the products impressive capability, whcih needs to be summed up in just an A4 brochure.
Key features to include....
-HD resolution of 1920 x 1080
-Screen sizes of 55,65,70 and 84"
-Capture ideas/notes/ direct to internal memory or USB
-Annotate over presentations and save/email/share
-20-point touch (for multiple users at the same time)
-inbuilt Orvix-(brouse the web, access Apps)
-Anti-scratch/Anti-glare screen
-Q-Flow wifi for sharing direct from smartphones/tablets
-Multiple inputs for other devices

Special Offer
Fully installed 55” kyvex with wall bracket, USB/VGA/HDMI wall plate and all cabling from only $85.00 inc GST per week for 24 months.(conditions apply)

Design should include company logo, carry across our "BLUE" corporate feel. and contact details (phone, email and web)

Images and previous brochure attached for corporate feel etc.
We feel that some stock images might be required to convey the touchscreen being used in a corporate/professional environment might be required, happy to take your advise on this and purchase if required.

Target Market(s)

Corporate, finance and government

Industry/Entity Type

Government

Font styles to use
Serif
Sans Serif

Colors
3377b5
0255a3

Requirements
Must have
• Be attention-grabbing using the technology and simplicity of the product to gain interest to prospective buyers interested in showing their customers or staff they are an industry leader by adopting technology. Must carry the same Tolk group corporate feel as previous brochure (attached as sample).
Should not have
• Be cluttered and confusing. Not look like the existing kyvex brochure which is targeted towards education and schools. This product has enormous potential for the business, corporate and government sectors.

```html
<!DOCTYPE html>
<html lang="en">
<head>
<meta charset="utf-8">
<title>Kyvex brochure – Tolk group systems</title>
<link href="https://fonts.googleapis.com/css2?family=Open+Sans:ital,wght@0,400;0,600;1,600;1,700&family=PT+Serif:ital,wght@0,400;0,700;1,400&display=swap" rel="stylesheet">
<style>
  :root{
    --blue-deep:#0a4fd8;
    --blue-mid:#1266e6;
    --blue-light:#1a9af2;
    --cyan:#19e3f5;
    --cyan-soft:#6fd9f2;
    --card:#f7f8fa;
    --feature-text:#1a6fd6;
    --white:#ffffff;
    --ink:#0b0b14;
    --offer-blue:#1240c8;
  }
  *{margin:0;padding:0;box-sizing:border-box}
  html,body{width:1200px;height:849px;overflow:hidden;background:#fff}
  .brochure{position:relative;width:1200px;height:849px;overflow:hidden;background:var(--blue-deep)}
  .backdrop{position:absolute;inset:0}

  /* Features card */
  .features{position:absolute;left:14px;top:168px;width:342px;height:504px;background:var(--card);border-radius:26px;padding:10px 26px 0 30px;font-family:"Open Sans",Arial,sans-serif;color:var(--feature-text)}
  .features__accent{position:absolute}
  .features__accent--top{right:-12px;top:-12px;width:170px;height:170px}
  .features__accent--bottom{left:-8px;bottom:-10px;width:90px;height:96px}
  .features h2{font-size:19px;font-style:italic;font-weight:700;margin:8px 0 11px;position:relative}
  .features ul{list-style:none;position:relative}
  .features li{font-size:17.4px;line-height:24px;margin-bottom:11.2px}

  /* Offer panel */
  .offer-banner{position:absolute;left:450px;top:186px;width:300px;height:96px}
  .offer-banner span{position:absolute;left:26px;top:19px;font-family:"PT Serif",Georgia,serif;font-size:34px;color:var(--offer-blue);letter-spacing:.3px;transform:rotate(2deg);transform-origin:left}
  .offer-text{position:absolute;left:476px;top:273px;width:260px;text-align:center;font-family:"PT Serif",Georgia,serif;font-style:italic;font-size:16px;line-height:21.6px;color:var(--white)}

  .contact{position:absolute;left:400px;top:578px;width:400px;text-align:center;color:var(--white)}
  .contact__phone{font-family:"PT Serif",Georgia,serif;font-size:41px;line-height:56px}
  .contact__tagline{font-family:"PT Serif",Georgia,serif;font-style:italic;font-size:17px;margin-top:2px}
  .contact__line{font-family:"Open Sans",Arial,sans-serif;font-size:16px;line-height:35px}
  .contact__web{margin-top:8px}

  /* Photo panel */
  .photo{position:absolute;background:var(--white);padding:12px 12px 22px;box-shadow:0 4px 10px rgba(0,0,40,.35)}
  .photo__fill{width:100%;height:100%}
  .photo--one{left:944px;top:116px;width:216px;height:196px;transform:rotate(-8deg)}
  .photo--one .photo__fill{background:linear-gradient(135deg,#c9cfd8,#1d3e7a 45%,#0b1f3c)}
  .photo--three{left:976px;top:344px;width:208px;height:212px;transform:rotate(3deg)}
  .photo--three .photo__fill{background:linear-gradient(160deg,#3a6fb0,#8ec6ea 50%,#1c3f6e)}
  .photo--two{left:816px;top:300px;width:226px;height:222px;transform:rotate(-7deg)}
  .photo--two .photo__fill{background:linear-gradient(150deg,#dfeaf5,#b6cfe6 55%,#5a7fa8)}

  .brand{position:absolute;left:800px;top:624px;width:400px;height:92px;background:var(--white);display:flex;align-items:center;justify-content:flex-end;padding-right:18px;gap:14px}
  .brand__mark{width:20px;height:20px;background:#2ec4c8}
  .brand__name{font-family:"Open Sans",Arial,sans-serif;font-size:31px;font-weight:400;color:var(--ink)}
  .brand__slogan{position:absolute;left:800px;top:728px;width:400px;text-align:center;font-family:"PT Serif",Georgia,serif;font-weight:700;font-size:21px;line-height:28px;color:var(--ink)}
</style>
</head>
<body>
<main class="brochure">
  <svg class="backdrop" width="1200" height="849" viewBox="0 0 1200 849" aria-hidden="true">
    <defs>
      <linearGradient id="panel-left" x1="0" y1="0" x2="0" y2="1">
        <stop offset="0" stop-color="#1260e0"/><stop offset="1" stop-color="#0d4fd6"/>
      </linearGradient>
      <linearGradient id="panel-middle" x1="0" y1="0" x2="0" y2="1">
        <stop offset="0" stop-color="#1d9ef4"/><stop offset=".45" stop-color="#1069ea"/><stop offset="1" stop-color="#1a7ce8"/>
      </linearGradient>
      <linearGradient id="panel-right" x1="0" y1="0" x2="0" y2="1">
        <stop offset="0" stop-color="#0e5ae6"/><stop offset="1" stop-color="#0a47d6"/>
      </linearGradient>
      <linearGradient id="streak" x1="0" y1="0" x2="1" y2="0">
        <stop offset="0" stop-color="#19e3f5" stop-opacity=".2"/><stop offset=".5" stop-color="#19e3f5" stop-opacity=".85"/><stop offset="1" stop-color="#19e3f5" stop-opacity=".3"/>
      </linearGradient>
    </defs>
    <rect x="0" y="0" width="400" height="849" fill="url(#panel-left)"/>
    <rect x="400" y="0" width="400" height="849" fill="url(#panel-middle)"/>
    <rect x="800" y="0" width="400" height="849" fill="url(#panel-right)"/>
    <polygon points="0,54 1200,200 1200,212 0,66" fill="url(#streak)" opacity=".6"/>
    <polygon points="300,96 1040,170 960,196 340,124" fill="#19e3f5" opacity=".45"/>
    <polygon points="1200,0 1200,20 1000,150 980,150" fill="#19e3f5" opacity=".55"/>
    <polygon points="0,500 400,120 400,150 0,560" fill="#ffffff" opacity=".06"/>
    <polygon points="600,110 860,110 860,200 600,200" fill="#0b3fc8" opacity=".25"/>
    <polygon points="0,720 1200,800 1200,818 0,740" fill="url(#streak)" opacity=".7"/>
    <polygon points="60,690 520,760 520,780 80,712" fill="#19e3f5" opacity=".5"/>
    <polygon points="0,849 120,690 140,690 20,849" fill="#19e3f5" opacity=".55"/>
    <polygon points="480,849 800,700 800,720 520,849" fill="#ffffff" opacity=".08"/>
    <polygon points="516,116 528,128 514,128" fill="#fff"/>
    <polygon points="720,128 730,134 720,140" fill="#fff"/>
    <polygon points="462,408 470,418 458,422" fill="#fff"/>
    <polygon points="702,450 714,456 710,466" fill="#fff"/>
  </svg>

  <section class="features">
    <svg class="features__accent features__accent--top" viewBox="0 0 170 170" aria-hidden="true">
      <path d="M30 0 H150 Q170 0 170 20 V150 Q170 170 150 166 H140 V48 Q140 30 122 30 H22 Q0 30 6 12 Q10 0 30 0Z" fill="#5bc6e6"/>
    </svg>
    <svg class="features__accent features__accent--bottom" viewBox="0 0 90 96" aria-hidden="true">
      <path d="M14 0 H24 V66 Q24 80 40 80 H90 V96 H20 Q0 96 0 76 V12 Q0 0 14 0Z" fill="#5bc6e6"/>
    </svg>
    <h2>Key Features</h2>
    <ul>
      <li>HD resolution of 1920 x 1080</li>
      <li>Screen sizes of 55,65,70 and 84"</li>
      <li>Capture ideas/notes/ direct to internal memory or USB</li>
      <li>Annotate over presentations and save/email/share</li>
      <li>20-point touch (for multiple users at the same time)</li>
      <li>inbuilt Orvix-(brouse the web, access Apps)</li>
      <li>Anti-scratch/Anti-glare screen</li>
      <li>Q-Flow wifi for sharing direct from smartphones/tablets</li>
      <li>Multiple inputs for other devices</li>
    </ul>
  </section>

  <div class="offer-banner">
    <svg width="300" height="96" viewBox="0 0 300 96" aria-hidden="true">
      <polygon points="0,2 292,20 292,82 282,92 288,78 8,72 0,62" fill="#0a2fa0"/>
      <polygon points="6,0 292,18 292,76 6,68" fill="#ffffff"/>
    </svg>
    <span>SPECIAL OFFER</span>
  </div>
  <p class="offer-text">Fully installed 55” kyvex<br>with wall bracket,<br>USB/VGA/HDMI wall plate<br>and all cabling from only<br>$85.00 inc GST per week for<br>24 months. (conditions apply)</p>

  <section class="contact">
    <p class="contact__phone">1300 555 019</p>
    <p class="contact__tagline">“Connecting People With Technology”</p>
    <p class="contact__line contact__web">www.tolksystems.com.au</p>
    <p class="contact__line">info@tolksystems.com.au</p>
    <p class="contact__line">MELBOURNE | SYDNEY</p>
    <p class="contact__line">BRISBANE | PERTH</p>
  </section>

  <figure class="photo photo--one"><div class="photo__fill" role="img" aria-label="Photo: businesswoman with a tablet facing a large interactive screen"></div></figure>
  <figure class="photo photo--three"><div class="photo__fill" role="img" aria-label="Photo: hand touching a large digital touchscreen"></div></figure>
  <figure class="photo photo--two"><div class="photo__fill" role="img" aria-label="Photo: businesswoman with a laptop and floating app icons"></div></figure>

  <div class="brand">
    <span class="brand__mark"></span>
    <span class="brand__name">tolk group systems</span>
  </div>
  <p class="brand__slogan">PROFESSIONAL<br>AUDIO VISUAL SOLUTIONS</p>
</main>
</body>
</html>
```